Ecommerce Site for High End Watch repair

This high profile storefront is located in the heart of Manhattan and needs a complete new HIG H END look that will generate leads and sales for Vintage watches, straps and repairs of all kinds of watches.

The design should be based around the attached new logo, we will need to see the home page, a product results page with 4 watches at desktop view (1920x1080), a product detail view with the options to view multiple images, zoom in on images and have multiple upsell ability for straps, water proofing and customer reviews, plus a check out view. Flexible responsive Mobile/Tablet/Desktop design is imperative. Here are some competitors sites that the client likes
https://www.velmorastudio.example/
https://www.plinquaro.example/
https://www.drestwickandloom.example/
https://www.tuvenshoppe.example/
The Client is Ostrelle Hollow Watch, they do not have such a a large inventory as some of their competition but want to give the perception of top quality

We have a proprietary CMS in which we will implement your design so final product will need the fonts, graphics, color specifications and any other specialized css needed to produce the look.

Target Market(s)

high earners who like high end toys and fashionable clothes, watch collectors

Number of Pages Required

4 page

Requirements
Must have
• Home page that excites and at the same time shows intuitive navigation for the rest of the site
Product results page with high detail in each of 4 images
product detail page with multiple image view possibilities
Check out page with intuitive layout
Mobile view optimized
Highlight of repair services as well as sales
Nice to have
• customer reviews/testimonials
ways to display the watch detail innovatively
Place holders on the product detail page to upsell a wtch strap or add one of the services such as waterproofing or extended warranty

```html
<!DOCTYPE html>
<html lang="en">
<head>
<meta charset="utf-8">
<title>Ostrelle Hollow Watch — Home</title>
<link href="https://fonts.googleapis.com/css2?family=Cinzel:wght@400;500&family=Lato:wght@400;700&display=swap" rel="stylesheet">
<style>
:root{
  --ink:#1f1f1f;
  --text:#333333;
  --muted:#8a8a8a;
  --line:#cfcfcf;
  --band:#f1f1f1;
  --white:#ffffff;
  --dark:#222222;
  --night:#14161c;
  --gold:#c9a14a;
  --star:#f5c518;
}
*{box-sizing:border-box;margin:0;padding:0}
html,body{width:1200px;height:4508px;overflow:hidden;background:var(--white)}
body{position:relative;font-family:'Lato',sans-serif;color:var(--text)}
.abs{position:absolute}
.serif{font-family:'Cinzel',serif}
a{color:inherit;text-decoration:none}

/* hero */
.hero{left:0;top:0;width:1200px;height:770px;
  background:radial-gradient(ellipse at 78% 40%,#6b6f78 0%,#3a3d45 28%,#1d2028 60%,#101219 100%)}
.hero-base{left:0;top:560px;width:1200px;height:210px;background:linear-gradient(180deg,rgba(30,40,60,0) 0%,#2a3a55 60%,#1b2536 100%)}
.hero-watch{left:650px;top:90px;width:340px;height:680px;border-radius:160px 160px 40px 40px;
  background:radial-gradient(circle at 50% 38%,#e8e6df 0%,#b9b3a4 22%,#8c7a4c 40%,#4d4a45 70%,rgba(40,40,45,0) 100%)}
.brand{left:150px;top:22px;width:160px;text-align:center;color:var(--white)}
.brand .mark{width:40px;height:40px;border:1.5px solid currentColor;border-radius:50%;margin:0 auto 6px}
.brand .name{font-family:'Cinzel',serif;font-size:13px;line-height:15px;letter-spacing:1px}
.nav{top:56px;left:600px;display:flex;gap:0;font-size:13px;color:var(--white);letter-spacing:1px}
.nav a{position:absolute;white-space:nowrap}
.nav-icons{top:54px;left:932px;width:130px;height:24px}
.hero-title{left:150px;top:318px;font-family:'Cinzel',serif;font-size:50px;color:var(--white);letter-spacing:1px;white-space:nowrap}
.hero-sub{left:152px;top:388px;font-size:12px;color:var(--white)}
.btn{display:flex;align-items:center;justify-content:center;font-size:11px;letter-spacing:2px;text-transform:uppercase}
.btn-light{left:152px;top:433px;width:160px;height:38px;background:var(--white);color:var(--ink)}
.btn-dark{background:var(--dark);color:var(--white)}
.dots{display:flex;gap:6px}
.dots span{width:9px;height:9px;border:1.5px solid var(--white)}
.dots span.on{background:var(--white)}

/* features */
.feature{top:822px;width:220px;text-align:center}
.feature .icon{width:96px;height:96px;border-radius:50%;background:var(--dark);margin:0 auto;display:flex;align-items:center;justify-content:center}
.feature h3{font-family:'Cinzel',serif;font-weight:400;font-size:19px;color:var(--ink);margin-top:26px;letter-spacing:.5px}
.feature p{font-size:11px;line-height:13px;color:var(--muted);margin:6px auto 0;width:205px;height:56px}
.feature a{font-size:11px;text-decoration:underline;color:var(--text);letter-spacing:.5px}
.vrule{top:836px;width:1px;height:220px;background:var(--line)}

/* about & repair */
.band{left:0;width:1200px;background:var(--band)}
.frame{border:2px solid var(--line)}
.photo-watch-dark{background:radial-gradient(ellipse at 45% 40%,#7a6a62 0%,#3a3130 30%,#1a1616 60%,#5a1a1e 100%)}
.photo-movement{background:radial-gradient(ellipse at 55% 55%,#f2d38a 0%,#c99236 35%,#8a5a1e 65%,#3a2410 100%)}
.eyebrow{font-family:'Cinzel',serif;font-size:18px;letter-spacing:9px;color:var(--ink)}
.section-title{font-family:'Cinzel',serif;font-weight:400;color:var(--ink);white-space:nowrap}
.copy{font-size:11.5px;line-height:26px;color:var(--text)}

/* products */
.heading-row{left:150px;width:900px;display:flex;align-items:center}
.heading-row h2{font-family:'Cinzel',serif;font-weight:400;font-size:30px;color:var(--ink);white-space:nowrap}
.heading-row .rule{flex:1;height:1px;background:var(--line);margin:6px 24px 0}
.heading-row a{font-size:11px;letter-spacing:1.5px;text-decoration:underline;color:var(--text);margin-top:6px}
.card-hi{background:#f4f4f4;box-shadow:0 2px 10px rgba(0,0,0,.15)}
.product{width:240px;text-align:center}
.product .img{margin:0 auto;border-radius:40px}
.product h4{font-family:'Cinzel',serif;font-weight:500;font-size:13.5px;color:var(--ink);line-height:17px}
.product .price{font-family:'Cinzel',serif;font-size:13px;color:var(--muted);margin-top:10px}
.watch-gold{background:linear-gradient(180deg,#7a4a2a 0%,#7a4a2a 25%,#e9dfb5 35%,#d6b760 55%,#e9dfb5 65%,#7a4a2a 75%,#5a3420 100%)}
.watch-steel{background:linear-gradient(180deg,#bdbdbd 0%,#8f8f8f 25%,#2a2a2a 38%,#1a1a1a 55%,#3a3a3a 68%,#a0a0a0 78%,#cfcfcf 100%)}
.watch-silver{background:linear-gradient(180deg,#2a2a2a 0%,#2a2a2a 25%,#dcdcdc 35%,#b5b5b5 55%,#dcdcdc 68%,#2a2a2a 76%,#1a1a1a 100%)}
.strap{height:56px;border-radius:18px;transform:rotate(32deg)}
.strap-cognac{background:linear-gradient(90deg,#4a1c12,#7a2e1c)}
.strap-toast{background:linear-gradient(90deg,#7a2c14,#b3512a)}
.strap-black{background:linear-gradient(90deg,#0e0e0e,#2a2a2a)}
.strap-nude{background:linear-gradient(90deg,#b98548,#e0b06c)}

/* brands */
.brand-name{top:3598px;width:220px;text-align:center;font-family:'Cinzel',serif;font-size:28px;color:var(--ink);letter-spacing:3px}

/* reviews */
.reviews{left:0;top:3677px;width:1200px;height:428px;background:radial-gradient(ellipse at 60% 20%,#3a3a3a 0%,#232323 45%,#1a1a1a 100%)}
.quote{left:180px;top:3844px;width:840px;text-align:center;font-size:11.5px;line-height:31px;color:var(--white)}
.qmark{font-family:'Cinzel',serif;font-size:48px;color:var(--white);line-height:1}

/* footer */
.foot-h{font-family:'Cinzel',serif;font-size:12.5px;color:var(--ink);letter-spacing:.5px}
.foot-list{font-size:11px;color:var(--text);line-height:31.5px;list-style:none}
.pay{font-size:10px;font-weight:700;color:var(--dark);letter-spacing:.5px}
</style>
</head>
<body>

<!-- HERO -->
<header>
  <div class="abs hero" role="img" aria-label="Two-tone gold and steel luxury wristwatch photographed against a dark city backdrop"></div>
  <div class="abs hero-base" aria-hidden="true"></div>
  <div class="abs hero-watch" aria-hidden="true"></div>

  <div class="abs brand">
    <div class="mark"></div>
    <div class="name">Ostrelle Hollow<br>Watch</div>
  </div>

  <nav class="abs nav" style="left:0;top:56px">
    <a style="left:602px">About</a>
    <a style="left:677px">Services</a>
    <a style="left:770px">Shop</a>
    <a style="left:837px">Contact</a>
  </nav>
  <svg class="abs nav-icons" viewBox="0 0 130 24" fill="none" stroke="#fff" stroke-width="1.6">
    <circle cx="10" cy="10" r="6"/><line x1="14.5" y1="14.5" x2="19" y2="19"/>
    <path d="M56 5h3l3 11h10l2-8H61"/><circle cx="64" cy="19" r="1.3"/><circle cx="71" cy="19" r="1.3"/>
    <circle cx="80" cy="9" r="5.5" fill="#fff" stroke="none"/>
    <text x="80" y="12" font-size="8" fill="#222" stroke="none" text-anchor="middle" font-family="Lato">2</text>
    <circle cx="112" cy="8" r="4.5"/><path d="M104 20c0-5 4-7 8-7s8 2 8 7z"/>
  </svg>

  <h1 class="abs hero-title">Luxury Watches</h1>
  <p class="abs hero-sub">Lorem Ipsum is simply dummy text of the printing and typesetting industry.</p>
  <a class="abs btn btn-light">Shop Now</a>
  <div class="abs dots" style="left:150px;top:562px"><span class="on"></span><span></span><span></span><span></span></div>
</header>

<!-- FEATURES -->
<section aria-label="Services">
  <div class="abs feature" style="left:131px">
    <div class="icon"><svg width="48" height="48" viewBox="0 0 48 48" fill="#fff"><rect x="17" y="4" width="14" height="10" rx="2"/><rect x="17" y="34" width="14" height="10" rx="2"/><circle cx="24" cy="24" r="12"/><circle cx="24" cy="24" r="7" fill="#222"/></svg></div>
    <h3>Watch Repair</h3>
    <p>Have your watch serviced by our master watchmakers.</p>
    <a>LEARN MORE</a>
  </div>
  <div class="abs vrule" style="left:355px"></div>
  <div class="abs feature" style="left:362px">
    <div class="icon"><svg width="52" height="52" viewBox="0 0 52 52" fill="#fff"><rect x="4" y="18" width="44" height="16" rx="5" transform="rotate(-35 26 26)"/><circle cx="20" cy="30" r="2" fill="#222"/><circle cx="26" cy="26" r="2" fill="#222"/><circle cx="32" cy="22" r="2" fill="#222"/></svg></div>
    <h3>Straps</h3>
    <p>Italian leather Straps</p>
    <a>VIEW STRAPS</a>
  </div>
  <div class="abs vrule" style="left:579px"></div>
  <div class="abs feature" style="left:593px">
    <div class="icon"><svg width="48" height="48" viewBox="0 0 48 48" fill="#fff"><rect x="18" y="3" width="12" height="11" rx="2"/><rect x="18" y="34" width="12" height="11" rx="2"/><circle cx="24" cy="24" r="12"/><path d="M24 17v8h5" stroke="#222" stroke-width="2" fill="none"/></svg></div>
    <h3>Vintage Watches</h3>
    <p>View our current inventory of expertly restored Vintage Watches.</p>
    <a>VIEW WATCHES</a>
  </div>
  <div class="abs vrule" style="left:827px"></div>
  <div class="abs feature" style="left:843px">
    <div class="icon"><svg width="44" height="44" viewBox="0 0 44 44" fill="#fff"><circle cx="22" cy="14" r="9"/><path d="M6 40c0-10 7-15 16-15s16 5 16 15z"/></svg></div>
    <h3>My Account</h3>
    <p>Login to view your existing repairs and collection of watches previously serviced at our state-of-the-art facility.</p>
    <a>LOGIN</a>
  </div>
</section>

<!-- ABOUT -->
<section aria-label="About">
  <div class="abs band" style="top:1111px;height:486px"></div>
  <div class="abs photo-watch-dark" style="left:150px;top:1203px;width:417px;height:441px" role="img" aria-label="Bronze-toned wristwatch resting on a red cloth in dim light"></div>
  <div class="abs frame" style="left:136px;top:1191px;width:418px;height:437px"></div>
  <div class="abs eyebrow" style="left:631px;top:1208px">About</div>
  <h2 class="abs section-title" style="left:631px;top:1240px;font-size:26px">Ostrelle Hollow Watch</h2>
  <p class="abs copy" style="left:631px;top:1303px;width:425px">Lorem Ipsum is simply dummy text of the printing and typesetting industry. Lorem Ipsum has been the industry's standard dummy text ever since the 1500s, when an unknown printer took a galley of type and scrambled it to make a type specimen book. It has survived not only five centuries, but also the leap into electronic typesetting, remaining essentially unchanged.</p>
  <a class="abs btn btn-dark" style="left:631px;top:1473px;width:160px;height:40px">Shop Now</a>
</section>

<!-- NEW ARRIVALS -->
<section aria-label="New arrivals">
  <div class="abs heading-row" style="top:1752px"><h2>New Arrivals</h2><span class="rule"></span><a>VIEW ALL PRODUCTS</a></div>
  <div class="abs card-hi" style="left:362px;top:1842px;width:252px;height:409px"></div>

  <div class="abs product" style="left:118px;top:1863px">
    <div class="img watch-gold" role="img" aria-label="Gold dress watch with brown leather strap" style="width:110px;height:231px"></div>
    <h4 style="margin-top:30px">Valcourt 3251</h4><div class="price">$190.00</div>
  </div>
  <div class="abs product" style="left:368px;top:1863px">
    <div class="img watch-steel" role="img" aria-label="Black dial chronograph on steel bracelet" style="width:140px;height:231px"></div>
    <h4 style="margin-top:30px">1964 Grey No Date</h4><div class="price">$250.00</div>
    <a class="btn btn-dark" style="margin:24px auto 0;width:157px;height:38px">Add to Cart</a>
  </div>
  <div class="abs product" style="left:620px;top:1863px">
    <div class="img watch-gold" role="img" aria-label="Gold moonphase chronograph with tan leather strap" style="width:130px;height:231px"></div>
    <h4 style="margin-top:30px">Chrono Sport 4114</h4><div class="price">$3500.00</div>
  </div>
  <div class="abs product" style="left:847px;top:1863px">
    <div class="img watch-silver" role="img" aria-label="Silver dial watch with black leather strap" style="width:150px;height:231px"></div>
    <h4 style="margin-top:30px">Merrow Tane MT47-D04</h4><div class="price">$75.00</div>
  </div>
</section>

<!-- REPAIR -->
<section aria-label="Repair services">
  <div class="abs band" style="top:2358px;height:484px"></div>
  <h2 class="abs section-title" style="left:152px;top:2462px;font-size:27px;line-height:38px">Professional Watch<br>Repair Services</h2>
  <p class="abs copy" style="left:152px;top:2558px;width:420px">From battery replacement to fully servicing your watch to bring it back to it's original new condition. Including antique watch repair, watch restoration, pocket watch repair, Brandt watch repair, Kestrel watch repair, Marlowe watch repair, Dunmore watch repair, Varenne watch repair, and many more.</p>
  <a class="abs btn btn-dark" style="left:152px;top:2700px;width:158px;height:40px">Read More</a>
  <div class="abs photo-movement" style="left:633px;top:2449px;width:418px;height:441px" role="img" aria-label="Close-up of a watchmaker's tool working inside a gold watch movement"></div>
  <div class="abs frame" style="left:649px;top:2435px;width:421px;height:439px"></div>
</section>

<!-- ADD-ONS -->
<section aria-label="Popular add-ons">
  <div class="abs heading-row" style="top:2972px"><h2>Popular Add-ons</h2><span class="rule"></span><a>VIEW ALL PRODUCTS</a></div>
  <div class="abs card-hi" style="left:362px;top:3066px;width:252px;height:389px"></div>

  <div class="abs product" style="left:128px;top:3130px">
    <div class="img strap strap-cognac" role="img" aria-label="Cognac leather watch strap" style="width:200px"></div>
    <h4 style="margin-top:98px">Halden Strap in<br>Cognac 20x16</h4><div class="price">$55.00</div>
  </div>
  <div class="abs product" style="left:366px;top:3130px">
    <div class="img strap strap-toast" role="img" aria-label="Toast brown leather watch strap" style="width:200px"></div>
    <h4 style="margin-top:98px">Halden Strap in<br>Toast 20x16</h4><div class="price">$55.00</div>
    <a class="btn btn-dark" style="margin:24px auto 0;width:157px;height:39px">Add to Cart</a>
  </div>
  <div class="abs product" style="left:602px;top:3130px">
    <div class="img strap strap-black" role="img" aria-label="Black leather watch strap with white stitching" style="width:200px"></div>
    <h4 style="margin-top:98px">Wexley Strap in<br>Black White 20x16</h4><div class="price">$45.00</div>
  </div>
  <div class="abs product" style="left:833px;top:3130px">
    <div class="img strap strap-nude" role="img" aria-label="Nude tan leather watch strap" style="width:200px"></div>
    <h4 style="margin-top:98px">Wexley Strap in<br>Nude 18x16</h4><div class="price">$45.00</div>
  </div>
</section>

<!-- BRANDS -->
<section aria-label="Brands we service">
  <div class="abs band" style="top:3554px;height:123px"></div>
  <div class="abs brand-name" style="left:105px">Corvane</div>
  <div class="abs brand-name" style="left:373px">Tickel</div>
  <div class="abs brand-name" style="left:619px">Aurelon</div>
  <div class="abs brand-name" style="left:870px">Selvaine</div>
</section>

<!-- REVIEWS -->
<section aria-label="Customer reviews">
  <div class="abs reviews" role="img" aria-label="Dark blurred close-up of a steel watch bracelet"></div>
  <h2 class="abs section-title" style="left:0;width:1200px;text-align:center;top:3762px;font-size:31px;color:var(--white)">Customer's Reviews</h2>
  <div class="abs qmark" style="left:158px;top:3826px">“</div>
  <p class="abs quote">Lorem Ipsum is simply dummy text of the printing and typesetting industry. Lorem Ipsum has been the industry's standard dummy text ever since the 1500s, when an unknown printer took a galley of type and scrambled it to make a type specimen book. It has survived not only five centuries, but also the leap into electronic typesetting, remaining essentially unchanged.</p>
  <div class="abs qmark" style="left:812px;top:3910px">”</div>
  <div class="abs serif" style="left:0;width:1200px;text-align:center;top:3962px;font-size:17px;color:var(--white)">Calder</div>
  <div class="abs" style="left:0;width:1200px;text-align:center;top:3986px;font-size:11px;color:var(--star);letter-spacing:1px">★★★★★</div>
  <div class="abs dots" style="left:576px;top:4038px"><span class="on"></span><span></span><span></span></div>
</section>

<!-- FOOTER -->
<footer>
  <div class="abs brand" style="left:145px;top:4171px;width:170px;color:var(--ink)">
    <div class="mark"></div>
    <div class="name">Ostrelle Hollow<br>Watch</div>
  </div>
  <div class="abs" style="left:145px;top:4318px;display:flex;gap:22px">
    <span class="pay">PAYCARD</span><span class="pay">STRATA</span><span class="pay">PAYVAULT</span>
  </div>
  <div class="abs pay" style="left:145px;top:4336px">MERIDIA</div>

  <div class="abs foot-h" style="left:385px;top:4176px">Contact Info..</div>
  <svg class="abs" style="left:385px;top:4238px" width="16" height="70" viewBox="0 0 16 70" fill="#222">
    <path d="M8 1a6 6 0 0 0-6 6c0 5 6 11 6 11s6-6 6-11a6 6 0 0 0-6-6zm0 8.5a2.5 2.5 0 1 1 0-5 2.5 2.5 0 0 1 0 5z"/>
    <path d="M3 52c1-1 3-1 4 0l1 2c0 1-1 2-1 2 1 2 3 4 5 5 0 0 1-1 2-1l2 1c1 1 1 3 0 4-3 3-8-1-11-4s-5-7-2-9z" transform="translate(-1 -4)"/>
  </svg>
  <ul class="abs foot-list" style="left:422px;top:4232px">
    <li>18 Linden Arcade</li><li>Harbor City, HC 20417</li><li>(555) 014-2290</li>
  </ul>
  <div class="abs" style="left:385px;top:4332px;width:175px;height:1px;background:var(--line)"></div>
  <div class="abs" style="left:388px;top:4365px;display:flex;gap:22px">
    <span style="width:7px;height:7px;border-radius:50%;background:var(--ink)"></span>
    <span style="width:7px;height:7px;border-radius:50%;background:var(--ink)"></span>
    <span style="width:7px;height:7px;border-radius:50%;background:var(--ink)"></span>
    <span style="width:7px;height:7px;border-radius:50%;background:var(--ink)"></span>
    <span style="width:7px;height:7px;border-radius:50%;background:var(--ink)"></span>
    <span style="width:7px;height:7px;border-radius:50%;background:var(--ink)"></span>
  </div>

  <div class="abs foot-h" style="left:617px;top:4176px">Quick Links</div>
  <ul class="abs foot-list" style="left:618px;top:4232px"><li>Home</li><li>About</li><li>Services</li><li>Shop</li><li>Contact</li></ul>

  <div class="abs foot-h" style="left:766px;top:4176px">Business Hours</div>
  <ul class="abs foot-list" style="left:766px;top:4232px"><li>Mon: 9AM-4PM</li><li>Tue: 9AM-4PM</li><li>Wed: 9AM-4PM</li><li>Thur: 9AM-4PM</li><li>Fri, Sat &amp; Sun: Closed</li></ul>

  <div class="abs foot-h" style="left:950px;top:4176px">Accounts</div>
  <ul class="abs foot-list" style="left:950px;top:4232px"><li>Login</li><li>Register</li><li>My profile</li><li>My Cart</li><li>Checkout</li></ul>

  <div class="abs" style="left:150px;top:4423px;width:900px;height:1px;background:var(--line)"></div>
  <p class="abs" style="left:150px;top:4445px;font-size:10.5px;color:var(--text)">Copyright © 2021 Ostrelle Hollow Watch. All Right Reserved.</p>
  <p class="abs" style="left:862px;top:4445px;width:188px;text-align:right;font-size:10.5px;color:var(--text)">Privacy Policy - Terms &amp; Conditions</p>
</footer>

</body>
</html>
```